I need a business card design for my new clinic (SPORTS MEDICINE OF KNEE). I am orthopedist, expert in sports surgery, especially knee surgery. I prefer, as colors, the colors of my logo (green, black and white). I already have my logo and should appear on my card. It's good to see my site to have ideas (www.drlucianovarela.com)
It needs contain:
my name: Dr. Luciano Varela
my registration: CRM 584-902
my specialty: Cirurgia do Joelho / Esporte
my address: Centro Executivo - Pinheiral Plaza
Av. Doutor Augusto Brandão Cunha, 2740 sala 0836
Jd. Ipanema - Ribeirão Preto - SP
my phone number: Tel (16) 8245-3908
my clinic phone: (16) 3670-4851
my e-mail: drlucianovarela@mailbox-exemplo.com
my site: www.drlucianovarela.com

Target Market(s)

futures patients

Industry/Entity Type

Clinic

Requirements
Nice to have
• letters not overfilled
straight lines, with few curves

```html
<!DOCTYPE html>
<html lang="pt-BR">
<head>
<meta charset="utf-8">
<title>Dr. Luciano Varela – Cartão de visita</title>
<link rel="stylesheet" href="https://fonts.googleapis.com/css2?family=Mulish:wght@700&family=Questrial&display=swap">
<style>
  :root {
    --backdrop: #1c1c1c;
    --card-white: #ffffff;
    --card-grey: #e4e4e4;
    --ink-dark: #2b2b2b;
    --ink-grey: #7a7a7a;
    --brand-green: #55d69a;
    --brand-green-deep: #4dbb86;
    --brand-black: #141414;
  }
  * { box-sizing: border-box; margin: 0; padding: 0; }
  html, body {
    width: 1200px; height: 1000px; overflow: hidden;
    background: var(--backdrop);
    font-family: "Questrial", "Century Gothic", sans-serif;
  }
  .stage { position: relative; width: 1200px; height: 1000px; }

  .card {
    position: absolute; left: 250px; width: 700px; height: 400px;
    overflow: hidden;
  }

  /* ---------- Front ---------- */
  .card-front { top: 80px; background: var(--card-white); }
  .brand-square {
    position: absolute; left: 36px; top: 34px; width: 112px; height: 112px;
    background: var(--brand-black); border-radius: 14px;
  }
  .brand-name {
    position: absolute; left: 24px; top: 150px; width: 150px;
    font-size: 30px; letter-spacing: 2px; color: var(--brand-black);
    text-align: center;
  }
  .green-block {
    position: absolute; left: 0; top: 192px; width: 186px; height: 208px;
    background: linear-gradient(180deg, var(--brand-green) 0%, var(--brand-green) 82%, #9fe8c4 100%);
  }
  .doctor {
    position: absolute; right: 40px; top: 40px; text-align: right;
  }
  .doctor-name {
    font-family: "Mulish", Verdana, sans-serif; font-weight: 700;
    font-size: 22px; color: var(--ink-dark);
  }
  .doctor-crm { font-size: 16px; color: var(--ink-grey); margin-top: 2px; }
  .specialty {
    position: absolute; left: 214px; top: 138px;
    font-size: 25px; letter-spacing: 1px; color: var(--brand-green);
    text-transform: uppercase;
  }
  .contact {
    position: absolute; left: 214px; top: 210px;
    font-size: 16px; line-height: 23px; color: var(--ink-grey);
    list-style: none;
  }

  /* ---------- Back ---------- */
  .card-back {
    top: 520px;
    background: linear-gradient(180deg, var(--card-white) 0%, var(--card-grey) 100%);
  }
  .back-lockup {
    position: absolute; left: 190px; top: 120px;
    display: flex; align-items: center; gap: 18px;
  }
  .back-square {
    width: 80px; height: 80px; background: var(--brand-black); border-radius: 10px;
  }
  .back-name { font-size: 58px; letter-spacing: 3px; color: var(--brand-black); line-height: 1; }
  .back-tagline { font-size: 18px; color: var(--brand-green-deep); margin-top: 6px; letter-spacing: 1px; }
  .back-role {
    position: absolute; left: 0; right: 0; bottom: 44px;
    text-align: center; font-size: 17px; letter-spacing: 1px; color: var(--ink-dark);
  }
  .back-band {
    position: absolute; left: 0; right: 0; bottom: 0; height: 26px;
    background: var(--brand-green-deep);
  }
</style>
</head>
<body>
<main class="stage">

  <section class="card card-front" aria-label="Frente do cartão">
    <div class="brand-square" aria-hidden="true"></div>
    <div class="brand-name">VARELA</div>
    <div class="green-block" aria-hidden="true"></div>

    <div class="doctor">
      <p class="doctor-name">Dr. Luciano Varela</p>
      <p class="doctor-crm">CRM 584-902</p>
    </div>

    <p class="specialty">Cirurgia do Joelho / Esporte</p>

    <ul class="contact">
      <li>Centro Executivo - Pinheiral Plaza</li>
      <li>Av. Doutor Augusto Brandão Cunha, 2740 sala 0836</li>
      <li>Jd. Ipanema - Ribeirão Preto - SP</li>
      <li>TEL (16) 8245-3908, (16) 3670-4851</li>
      <li>E-MAIL: drlucianovarela@mailbox-exemplo.com</li>
      <li>WEB: www.drlucianovarela.com</li>
    </ul>
  </section>

  <section class="card card-back" aria-label="Verso do cartão">
    <div class="back-lockup">
      <div class="back-square" aria-hidden="true"></div>
      <div>
        <p class="back-name">VARELA</p>
        <p class="back-tagline">Traumatologia</p>
      </div>
    </div>
    <p class="back-role">ORTOPEDISTA - CIRURGIA DO JOELHO</p>
    <div class="back-band" aria-hidden="true"></div>
  </section>

</main>
</body>
</html>
```